Pedalwise Touring Co Brochure

We need an informational brochure designed to display all of our cycling tours for the 2019 season. The majority of text and images can be pulled from our website - www.pedalwisetouringco.example

We would like to use the colors red (#242424), Grey, and White

```html
<!DOCTYPE html>
<html lang="en">
<head>
<meta charset="utf-8">
<title>Pedalwise Touring Co Brochure Cover</title>
<link rel="stylesheet" href="https://fonts.googleapis.com/css2?family=Anton&family=Montserrat:wght@500;600&display=swap">
<style>
  :root {
    --stage: #2a2a2a;
    --sky-top: #6f5a7a;
    --sky-mid: #8d6f86;
    --earth: #6b3f30;
    --rock: #4a2a22;
    --deep: #2e1a17;
    --white: #ffffff;
    --band: rgba(255,255,255,0.16);
  }
  * { margin: 0; padding: 0; box-sizing: border-box; }
  html, body { width: 1200px; height: 1134px; overflow: hidden; background: var(--stage); }
  .cover {
    position: absolute; left: 200px; top: 47px; width: 800px; height: 1040px;
    overflow: hidden; color: var(--white);
    font-family: "Montserrat", sans-serif;
  }
  .cover-photo {
    position: absolute; inset: 0;
    background:
      radial-gradient(ellipse 70% 40% at 95% 30%, rgba(170,90,60,0.75), transparent 70%),
      radial-gradient(ellipse 90% 25% at 40% 2%, rgba(120,60,45,0.9), transparent 75%),
      linear-gradient(180deg, var(--rock) 0%, var(--sky-top) 16%, var(--sky-mid) 42%, var(--earth) 62%, var(--rock) 82%, var(--deep) 100%);
  }
  .brand {
    position: absolute; left: 70px; top: 150px;
    display: flex; align-items: center; gap: 22px;
  }
  .brand-circle {
    width: 110px; height: 110px; border-radius: 50%;
    border: 4px solid var(--white);
  }
  .brand-name {
    font-weight: 600; font-size: 34px; letter-spacing: 2px; line-height: 1.2;
    width: 260px;
  }
  .headline {
    position: absolute; left: 100px; top: 520px;
    font-family: "Anton", sans-serif; font-weight: 400; font-size: 74px; line-height: 1.04;
    letter-spacing: 1px; text-transform: uppercase;
  }
  .tagline {
    position: absolute; left: 104px; top: 695px; width: 520px;
    font-weight: 500; font-size: 19px; line-height: 1.3; letter-spacing: 0.6px;
  }
  .intro {
    position: absolute; left: 60px; right: 60px; top: 870px;
    text-align: center; font-weight: 500; font-size: 18px; line-height: 1.35; letter-spacing: 0.5px;
  }
  .url-band {
    position: absolute; left: 0; right: 0; top: 955px; height: 44px;
    background: var(--band);
    display: flex; align-items: center; justify-content: center;
    font-weight: 500; font-size: 18px; letter-spacing: 1px;
  }
</style>
</head>
<body>
  <section class="cover">
    <div class="cover-photo" role="img" aria-label="Mountain biker riding a red rock desert trail beneath a sandstone arch at dusk"></div>
    <div class="brand">
      <div class="brand-circle"></div>
      <div class="brand-name">Pedalwise Touring Co</div>
    </div>
    <h1 class="headline">It's all about<br>the ride</h1>
    <p class="tagline">Cycling and mountain bike adventures that turn your bucket list into a bike-it list</p>
    <p class="intro">Our cycling tours are designed for active to avid riders and pay<br>homage to the greatest biking routes in North America.<br>For those about to ride, we salute you.</p>
    <div class="url-band">www.pedalwisetouringco.example</div>
  </section>
</body>
</html>
```